Occupational Therapist does home accessibility for disabled folks; needs business card design

We need a business card for a company in Portland, Oregon that specializes in making homes accessible, comfortable, and functional for people who are disabled or aging who would like to stay in THEIR home. Our medical background as Occupational Therapists allows us to translate the functional needs of the person into the recommendations for the design of the home remodel.

Target Market(s)

Elderly, children of elderly
People with disabilities, families of people with disabilities

Industry/Entity Type

Business

Contact Information for Business Card

Company name: HomeWise
Name: Danielle Reyes Crawford, OTR/L, CAPS, ECHM
Occupational Therapist, Home Modification & Accessibility Specialist
website: www.homewiseforyears.com
email: homewiseforyears@nestmail.example
phone: (503)218-4057
CCB #: 487315

Font styles to use
Sans Serif

Requirements
Must have
• My logo
• Easy to read font with contrasting background
• Please list the Services offered: Occupational Therapy, Home safety & accessibility assessments, Home modification consulting, project management
Nice to have
• Friendly, welcoming feel
Should not have
• Dark colored background

```html
<!DOCTYPE html>
<html lang="en">
<head>
<meta charset="utf-8">
<title>HomeWise Business Card</title>
<link rel="stylesheet" href="https://fonts.googleapis.com/css2?family=Source+Sans+3:wght@400;600&display=swap">
<style>
  :root {
    --page: #ece9e5;
    --card: #ffffff;
    --ink: #1f1f1f;
    --slate: #5a5b5e;
    --slate-dark: #3f4043;
    --muted: #6b6b6b;
    --orange: #cf7119;
  }
  * { margin: 0; padding: 0; box-sizing: border-box; }
  html, body {
    width: 1200px; height: 1200px; overflow: hidden;
    background: var(--page);
    font-family: "Source Sans 3", "Myriad Pro", Arial, sans-serif;
  }
  .card {
    position: absolute; left: 75px; top: 300px;
    width: 1050px; height: 600px;
    background: var(--card);
    box-shadow: 0 10px 30px rgba(0,0,0,0.15);
    overflow: hidden;
  }
  .card-bands { position: absolute; inset: 0; }
  .brand {
    position: absolute; left: 70px; top: 250px;
    width: 400px;
    display: flex; align-items: center; gap: 16px;
  }
  .brand-mark { width: 40px; height: 40px; background: var(--orange); flex: none; }
  .brand-name {
    font-size: 64px; font-weight: 600; color: var(--slate-dark);
    line-height: 1; white-space: nowrap;
  }
  .divider {
    position: absolute; left: 500px; top: 85px;
    width: 4px; height: 320px; background: var(--slate-dark);
  }
  .person { position: absolute; left: 540px; top: 95px; }
  .person-name { font-size: 33px; font-weight: 600; color: var(--ink); line-height: 1.1; }
  .person-credentials { font-size: 23px; color: var(--muted); line-height: 1.2; margin-top: 4px; }
  .person-title { font-size: 24px; font-weight: 600; color: var(--orange); line-height: 1.2; margin-top: 2px; }
  .contact { position: absolute; left: 540px; top: 262px; list-style: none; }
  .contact li {
    display: flex; align-items: center; gap: 14px;
    font-size: 23px; color: var(--ink); height: 34px;
  }
  .contact-icon { width: 22px; height: 22px; flex: none; }
  .contact .plain { padding-left: 36px; }
</style>
</head>
<body>
  <div class="card">
    <svg class="card-bands" width="1050" height="600" viewBox="0 0 1050 600">
      <path d="M0 510 L525 500 L525 600 L0 600 Z" fill="var(--slate)"/>
      <path d="M560 438 L1050 428 L1050 438 L560 448 Z" fill="var(--slate-dark)"/>
      <path d="M545 600 L560 475 Q563 458 582 458 L1050 450 L1050 600 Z" fill="var(--orange)"/>
    </svg>

    <div class="brand">
      <span class="brand-mark"></span>
      <span class="brand-name">HomeWise</span>
    </div>

    <div class="divider"></div>

    <div class="person">
      <p class="person-name">Danielle Reyes Crawford</p>
      <p class="person-credentials">OTR/L, CAPS, ECHM</p>
      <p class="person-title">Occupational Therapist, Home<br>Modification &amp; Accessibility Specialist</p>
    </div>

    <ul class="contact">
      <li>
        <svg class="contact-icon" viewBox="0 0 22 22" aria-hidden="true">
          <rect width="22" height="22" rx="3" fill="var(--orange)"/>
          <path d="M7 5 L9.5 5 L10.5 8 L9 9.3 Q10.5 12.5 12.7 13 L14 11.5 L17 12.5 L17 15 Q16 17 13.5 16.5 Q7 14.5 5.5 8 Q5 6 7 5 Z" fill="#fff"/>
        </svg>
        (503)218-4057
      </li>
      <li>
        <svg class="contact-icon" viewBox="0 0 22 22" aria-hidden="true">
          <rect width="22" height="22" rx="3" fill="var(--orange)"/>
          <circle cx="11" cy="11" r="6" fill="none" stroke="#fff" stroke-width="1.6"/>
          <path d="M5 11 H17 M11 5 Q8 11 11 17 Q14 11 11 5" fill="none" stroke="#fff" stroke-width="1.3"/>
        </svg>
        www.homewiseforyears.com
      </li>
      <li>
        <svg class="contact-icon" viewBox="0 0 22 22" aria-hidden="true">
          <rect width="22" height="22" rx="3" fill="var(--orange)"/>
          <rect x="5" y="7" width="12" height="9" fill="none" stroke="#fff" stroke-width="1.5"/>
          <path d="M5 7 L11 12 L17 7" fill="none" stroke="#fff" stroke-width="1.5"/>
        </svg>
        homewiseforyears@nestmail.example
      </li>
      <li class="plain">CCB #: 487315</li>
    </ul>
  </div>
</body>
</html>
```